Create a Eye Catching Web Design

We need an informative web design that needs to be eye catching and unique. All of the information needs to be on that page - We have a shopfront setup in the next 2 weeks so the website needs to be ready asap. We are selling mainly rehabilitation aids and mobility products.

The website is main purpose is to inform customers about our range of products, address and phone number. This is an interim website until we get an ecommerce website setup. We are not looking for an ecommerce website, just simple, eye-catching and informative. clean, crisp and modern -target age 45-75 yo (men and women)

I have included our logo and brochure designed with our range of product categories.

The website needs to be designed, coded and setup completely as a finished product.

As soon as the website design is chosen, the chosen designer would need to get the website up and running. If the website design is chosen and great, we could use the same designer for the ecommerce build as well.

www.tolvenacare.com
www.tolvenacare.com.au

Reason: I haven't received as many designs but variations from the same designers.

Target Market(s)

45-75

Industry/Entity Type

Health And Wellness

Coding

Coded - Design and coding required

Number of Pages Required

2 page

Font styles to use
Sans Serif

Requirements
Nice to have
• clean design, modern feel - not cluttered - something unique. for the market age

```html
<!DOCTYPE html>
<html lang="en">
<head>
<meta charset="utf-8">
<title>Tolvena Care</title>
<link href="https://fonts.googleapis.com/css2?family=Poppins:wght@400;500;600;700&family=Open+Sans:wght@400;600&display=swap" rel="stylesheet">
<style>
:root{
  --red:#ec1c24;
  --ink:#1e2127;
  --body:#5a5f6a;
  --soft:#f5f6f8;
  --line:#e6e7ea;
  --footer:#2a2d36;
  --footer-text:#a9acb4;
  --white:#ffffff;
}
*{box-sizing:border-box;margin:0;padding:0}
html,body{width:706px;height:1200px;overflow:hidden;background:var(--white)}
body{position:relative;font-family:"Open Sans",Arial,sans-serif;color:var(--body)}
.abs{position:absolute}
h1,h2,h3,.brand,.nav a,.btn{font-family:"Poppins",Arial,sans-serif}

/* hero */
.hero{left:0;top:0;width:706px;height:310px;overflow:hidden}
.hero-photo{position:absolute;inset:0;background:
  radial-gradient(ellipse at 62% 55%,rgba(255,255,255,.55),rgba(255,255,255,0) 45%),
  linear-gradient(180deg,#eef2ea 0%,#9fc277 35%,#5f8f36 70%,#6e8d4c 100%)}
.hero-shade{position:absolute;left:0;top:0;width:706px;height:60px;background:linear-gradient(180deg,rgba(0,0,0,.18),rgba(0,0,0,0))}
.brand{left:52px;top:14px;color:var(--white);font-size:17px;font-weight:600;letter-spacing:.5px;display:flex;align-items:center;gap:6px}
.brand .dot{width:10px;height:10px;border-radius:50%;background:var(--white)}
.nav{left:257px;top:19px;display:flex;gap:17px}
.nav a{color:var(--white);font-size:6.6px;text-decoration:none;letter-spacing:.2px;position:relative}
.nav a.active::before{content:"";position:absolute;left:0;right:0;top:-19px;height:2px;background:var(--red)}
.phone{left:575px;top:9px;display:flex;align-items:center;gap:6px;color:var(--white)}
.phone .ring{width:22px;height:22px;border-radius:50%;background:rgba(255,255,255,.18);display:flex;align-items:center;justify-content:center}
.phone small{display:block;font-size:6.5px}
.phone strong{display:block;font-size:8.5px;font-weight:600}
.hero-title{left:156px;top:104px}
.hero-title .small{font-family:"Poppins",sans-serif;font-size:25px;font-weight:600;color:#4a4a4a;line-height:1}
.hero-title .big{font-family:"Poppins",sans-serif;font-size:42px;font-weight:700;color:var(--red);line-height:1.15;letter-spacing:.5px}
.arrow-btn{width:22px;height:22px;border-radius:50%;display:flex;align-items:center;justify-content:center}
.arrow-prev{left:605px;top:264px;background:rgba(255,255,255,.45)}
.arrow-next{left:632px;top:264px;background:var(--red)}

/* about */
.about{left:0;top:310px;width:706px;height:151px;background:var(--soft);text-align:center}
.section-title{font-size:14px;font-weight:400;color:var(--ink)}
.rule{display:block;width:12px;height:1.5px;background:var(--red);margin:5px auto 0}
.about .section-title{margin-top:32px}
.about p{font-size:7.4px;line-height:13px;width:390px;margin:9px auto 0}
.btn-outline{display:inline-block;margin-top:11px;width:84px;height:23px;border:1.5px solid var(--red);border-radius:12px;color:var(--red);font-size:6px;line-height:20px;font-weight:500}

/* products */
.products-photo{left:0;top:461px;width:301px;height:272px;background:linear-gradient(160deg,#dfead4 0%,#8fb767 40%,#5f8b3b 75%,#8e9a7e 100%)}
.products-card{left:244px;top:495px;width:167px;height:203px;background:var(--white);box-shadow:0 4px 18px rgba(0,0,0,.08);padding:20px 21px 0}
.products-card h3{font-size:8.4px;font-weight:500;color:var(--ink);letter-spacing:.2px;padding-bottom:10px;border-bottom:1px solid var(--line)}
.product-list{list-style:none}
.product-list li{display:flex;justify-content:space-between;align-items:center;height:26px;border-bottom:1px solid var(--line);font-size:7.3px;color:var(--body)}
.product-list li.current{color:var(--red)}
.btn-soft{display:block;margin-top:13px;height:23px;border-radius:12px;background:#fde8ea;color:var(--red);font-size:6px;font-weight:500;text-align:center;line-height:23px}
.available{left:441px;top:536px;width:215px}
.available h2{font-size:12.5px;font-weight:400;color:var(--ink)}
.available .rule{margin:5px 0 0}
.available p{font-size:7.2px;line-height:15px;margin-top:11px}
.available p+p{margin-top:5px}

/* testimonials */
.testimonials{left:0;top:733px;width:706px;height:183px;text-align:center}
.testimonials .section-title{margin-top:34px}
.quote-mark{font-family:Georgia,serif;font-size:34px;color:#d9dadd;line-height:1}
.quote-open{left:123px;top:62px}
.quote-close{left:556px;top:93px}
.testimonials p{position:absolute;left:150px;top:76px;width:430px;font-size:7.3px;line-height:13px}
.client{position:absolute;left:277px;top:113px;display:flex;align-items:center;gap:10px}
.client .line{width:54px;height:1px;background:var(--line)}
.avatar{width:37px;height:37px;border-radius:50%;background:radial-gradient(circle at 50% 40%,#8a7d6c,#3a3530)}
.client-info{text-align:left}
.client-info strong{display:block;font-family:"Poppins",sans-serif;font-size:9.5px;font-weight:600;color:var(--ink);letter-spacing:1px}
.client-info span{display:block;font-size:6.3px}

/* contact band */
.contact-band{left:0;top:916px;width:706px;height:105px;background:var(--red);color:var(--white)}
.contact-band h2{position:absolute;left:52px;top:34px;font-size:13.5px;font-weight:400;line-height:16px}
.contact-band .rule{position:absolute;left:52px;top:73px;margin:0;background:var(--white)}
.contact-item{position:absolute;top:38px;display:flex;align-items:center;gap:9px;font-size:9.5px}
.contact-item .ring{width:26px;height:26px;border-radius:50%;background:rgba(255,255,255,.15);display:flex;align-items:center;justify-content:center}
.btn-white{position:absolute;left:573px;top:40px;width:81px;height:25px;border-radius:13px;background:var(--white);color:var(--ink);font-size:6.6px;font-weight:500;display:flex;align-items:center;justify-content:center;gap:6px}

/* footer */
.site-footer{left:0;top:1021px;width:706px;height:179px;background:var(--footer);color:var(--footer-text)}
.footer-col{position:absolute;top:26px}
.footer-col h3{font-size:9.5px;font-weight:400;color:var(--white)}
.footer-col .rule{margin:4px 0 0;background:var(--white)}
.footer-col p{font-size:7.3px;line-height:13px;margin-top:12px}
.links{display:flex;gap:32px;margin-top:12px}
.links ul{list-style:none;font-size:7.3px;line-height:13px}
.social{display:flex;gap:6px;margin-top:9px}
.social span{width:14px;height:14px;border-radius:50%;background:#454954}
.social span.on{background:#5a2228}
.footer-bottom{position:absolute;left:52px;top:152px;width:602px;border-top:1px solid #3a3d47;padding-top:8px;display:flex;justify-content:space-between;font-size:6.8px;color:var(--white)}
.footer-bottom nav{display:flex;gap:18px}
</style>
</head>
<body>

<header class="hero abs">
  <div class="hero-photo" role="img" aria-label="Photo of a smiling man in a wheelchair pushed by a carer along a sunny tree-lined park path"></div>
  <div class="hero-shade"></div>
  <div class="brand abs">TOLVENA <span class="dot"></span></div>
  <nav class="nav abs">
    <a class="active">HOME</a><a>ABOUT</a><a>PRODUCTS</a><a>BLOGS</a><a>CONTACT</a>
  </nav>
  <div class="phone abs">
    <span class="ring"><svg width="10" height="10" viewBox="0 0 24 24"><path fill="#fff" d="M6.6 10.8a15 15 0 0 0 6.6 6.6l2.2-2.2a1 1 0 0 1 1-.25 11.4 11.4 0 0 0 3.6.57 1 1 0 0 1 1 1V20a1 1 0 0 1-1 1A17 17 0 0 1 3 4a1 1 0 0 1 1-1h3.5a1 1 0 0 1 1 1c0 1.25.2 2.45.57 3.6a1 1 0 0 1-.25 1z"/></svg></span>
    <div><small>Phone:</small><strong>02 6100 4821</strong></div>
  </div>
  <div class="hero-title abs">
    <div class="small">Tolvena</div>
    <div class="big">CARE</div>
  </div>
  <span class="arrow-btn arrow-prev abs"><svg width="8" height="8" viewBox="0 0 10 10"><path d="M9 5H1M4 2 1 5l3 3" stroke="#fff" fill="none" stroke-width="1"/></svg></span>
  <span class="arrow-btn arrow-next abs"><svg width="8" height="8" viewBox="0 0 10 10"><path d="M1 5h8M6 2l3 3-3 3" stroke="#fff" fill="none" stroke-width="1"/></svg></span>
</header>

<section class="about abs">
  <h2 class="section-title">About us<span class="rule"></span></h2>
  <p>Etiam rhoncus maecenas tempus tellus eget condimentum rhoncus sem quam semper libero sit amet adipiscing sem neque sed ipsum nam quam nun.</p>
  <span class="btn btn-outline">LEARN MORE</span>
</section>

<div class="products-photo abs" role="img" aria-label="Photo of an older woman standing with a walking frame on a garden path"></div>
<section class="products-card abs">
  <h3>OUR MAIN PRODUCTS</h3>
  <ul class="product-list">
    <li>Massage Recliners <svg width="8" height="6" viewBox="0 0 10 8"><path d="M0 4h9M6 1l3 3-3 3" stroke="#555" fill="none"/></svg></li>
    <li>Electric Scooters <svg width="8" height="6" viewBox="0 0 10 8"><path d="M0 4h9M6 1l3 3-3 3" stroke="#555" fill="none"/></svg></li>
    <li class="current">Walking Aids <svg width="8" height="6" viewBox="0 0 10 8"><path d="M0 4h9M6 1l3 3-3 3" stroke="#ec1c24" fill="none"/></svg></li>
    <li>Everyday Living Aids <svg width="8" height="6" viewBox="0 0 10 8"><path d="M0 4h9M6 1l3 3-3 3" stroke="#555" fill="none"/></svg></li>
  </ul>
  <span class="btn btn-soft">VIEW ALL PRODUCTS</span>
</section>
<section class="available abs">
  <h2>Available Products</h2><span class="rule"></span>
  <p>Etiam rhoncus maecenas tempus tellus eget condimentum rhoncus sem quam semper libero sit amet adipiscing sem neque sed ipsum nam quam nun.</p>
  <p>Tempus tellus eget condimentum rhoncus sem quam semper libero sit amet adipiscing sem neque sed ipsum.</p>
</section>

<section class="testimonials abs">
  <h2 class="section-title">Clients Testimonials<span class="rule"></span></h2>
  <span class="quote-mark quote-open abs">&ldquo;</span>
  <p>Curabitur ullamcorper ultricies nisi nam eget dui etiam rhoncus maecenas tempus tellus eget condimentum rhoncus sem quam semper libero, sit amet adipiscing sem neque sed ipsum.</p>
  <span class="quote-mark quote-close abs">&rdquo;</span>
  <div class="client">
    <span class="line"></span>
    <span class="avatar" role="img" aria-label="Client portrait"></span>
    <div class="client-info"><strong>Maren</strong><span>Monthly Subscriber</span></div>
  </div>
</section>

<section class="contact-band abs">
  <h2>Contact us for a<br>personal demonstration</h2>
  <span class="rule"></span>
  <div class="contact-item" style="left:238px">
    <span class="ring"><svg width="11" height="9" viewBox="0 0 12 9"><rect x=".5" y=".5" width="11" height="8" fill="none" stroke="#fff"/><path d="M.5 .5 6 5l5.5-4.5" fill="none" stroke="#fff"/></svg></span>
    hello@tolvenacare.com
  </div>
  <div class="contact-item" style="left:396px">
    <span class="ring"><svg width="9" height="12" viewBox="0 0 10 13"><path d="M5 12S1 7.5 1 5a4 4 0 0 1 8 0c0 2.5-4 7-4 7z" fill="none" stroke="#fff"/><circle cx="5" cy="5" r="1.4" fill="none" stroke="#fff"/></svg></span>
    52 Ferrell st, Orban.
  </div>
  <span class="btn btn-white">CONTACT US <svg width="8" height="6" viewBox="0 0 10 8"><path d="M0 4h9M6 1l3 3-3 3" stroke="#1e2127" fill="none"/></svg></span>
</section>

<footer class="site-footer abs">
  <div class="footer-col" style="left:52px;width:180px">
    <h3>About us</h3><span class="rule"></span>
    <p>Maecenas nec odio et ante tincidunt tempus donec vitae sapien ut libero venenatis faucibus nullam quis ante etiam sit.</p>
  </div>
  <div class="footer-col" style="left:277px">
    <h3>Quick Links</h3><span class="rule"></span>
    <div class="links">
      <ul><li>Home</li><li>About us</li><li>Our Team</li><li>Latest News</li><li>Blogs</li></ul>
      <ul><li>Gallery</li><li>Products</li><li>E Commerce Store</li></ul>
    </div>
  </div>
  <div class="footer-col" style="left:493px;width:162px">
    <h3>Always listening</h3><span class="rule"></span>
    <p>The Tolvena Care team is always here to help. If you have any questions you can find us here.</p>
    <div class="social"><span class="on"></span><span></span></div>
  </div>
  <div class="footer-bottom">
    <span>&copy; 2017, All Rights Reserved.</span>
    <nav><span>Terms &amp; Conditions</span><span>Contact us</span><span>Login</span></nav>
  </div>
</footer>

</body>
</html>
```